Stationary - Business Card/Letterhead and envelope design

Details for my new Stationery Design Project will be added soon. , I have two logos I am trying to decide on. I will upload the eps logos shortly. I have attached a file of what i have so far. I need urgently Business cards, but also will need a letterhead template and envelopes.

PLEASE NOTE THE DEADLINE SAYS 2 DAYS but I need business card design in LESS THAN A DAY.

thanks, Details for my new Stationery Design Project will be added soon. , I have two logos I am trying to decide on. I will upload the eps logos shortly. I have attached a file of what i have so far. I need urgently Business cards, but also will need a letterhead template and envelopes.

thanks
Updates

I have uploaded one of the logos you can work with. hopefully the other one comes soon.

details for the business card.

Marla Thorne

Managing Director

P&K Ventures Ltd

Bda: 1-441-555-0193

Email: marla@pkvnbda.com

web: www.pkvnbda.com

Industry/Entity Type

Business

```html
<!DOCTYPE html>
<html lang="en">
<head>
<meta charset="utf-8">
<title>P&amp;K Ventures – Business Card</title>
<link rel="stylesheet" href="https://fonts.googleapis.com/css2?family=Arimo:wght@400;700&family=Michroma&family=Oswald:wght@600&display=swap">
<style>
  :root {
    --stage: #8c8c8c;
    --navy: #0d3a5c;
    --green: #568a3d;
    --steel: #4d6a8a;
    --paper: #ffffff;
    --ink: #1c1c1c;
    --label: #ffffff;
  }
  * { margin: 0; padding: 0; box-sizing: border-box; }
  html, body { width: 1200px; height: 1200px; overflow: hidden; }
  body {
    background: var(--stage);
    font-family: "Arimo", Arial, sans-serif;
    display: flex;
    flex-direction: column;
    align-items: center;
    padding-top: 28px;
  }
  .side-label {
    font-family: "Oswald", "Arial Narrow", sans-serif;
    font-weight: 600;
    font-size: 30px;
    color: var(--label);
    height: 44px;
    line-height: 44px;
    margin-bottom: 6px;
  }
  .card {
    position: relative;
    width: 860px;
    height: 491px;
    overflow: hidden;
    box-shadow: 0 4px 14px rgba(0,0,0,0.25);
  }
  .card + .side-label { margin-top: 34px; }

  /* back side */
  .card--back { background: var(--paper); }
  .accent-band {
    position: absolute;
    top: 0;
    right: 0;
    width: 300px;
    height: 36px;
    background: var(--navy);
  }
  .accent-rule {
    position: absolute;
    top: 46px;
    right: 0;
    width: 300px;
    height: 10px;
    background: var(--green);
  }
  .brand {
    position: absolute;
    left: 60px;
    top: 200px;
    display: flex;
    align-items: center;
    gap: 16px;
  }
  .brand-mark { width: 34px; height: 34px; background: var(--navy); }
  .brand-name {
    font-weight: 700;
    font-size: 40px;
    color: var(--navy);
    letter-spacing: 1px;
  }
  .company-details {
    position: absolute;
    left: 60px;
    top: 352px;
    font-size: 21px;
    font-weight: 700;
    line-height: 1.3;
    color: var(--ink);
  }

  /* front side */
  .card--front { background: var(--navy); }
  .side-band {
    position: absolute;
    left: 0;
    top: 0;
    bottom: 0;
    width: 120px;
    background: var(--green);
  }
  .side-rule {
    position: absolute;
    left: 140px;
    top: 0;
    bottom: 0;
    width: 12px;
    background: var(--steel);
  }
  .person {
    position: absolute;
    right: 56px;
    top: 44px;
    color: var(--paper);
  }
  .person-name {
    font-family: "Michroma", "Arial", sans-serif;
    font-size: 38px;
    line-height: 1.2;
  }
  .person-title { font-size: 20px; margin-top: 2px; }
  .contact {
    position: absolute;
    right: 54px;
    bottom: 62px;
    text-align: right;
    color: var(--paper);
    font-size: 22px;
    line-height: 1.3;
  }
</style>
</head>
<body>
  <div class="side-label">Back</div>
  <section class="card card--back">
    <div class="accent-band"></div>
    <div class="accent-rule"></div>
    <div class="brand">
      <span class="brand-mark"></span>
      <span class="brand-name">P&amp;K VENTURES</span>
    </div>
    <div class="company-details">
      <p>www.pkvnbda.com</p>
      <p>Address: 2/114Lorem Ipsum,</p>
      <p>Country Name Lorem</p>
    </div>
  </section>

  <div class="side-label">Front</div>
  <section class="card card--front">
    <div class="side-band"></div>
    <div class="side-rule"></div>
    <div class="person">
      <p class="person-name">Marla Thorne</p>
      <p class="person-title">Designation</p>
    </div>
    <div class="contact">
      <p>Ph. 1-441-555-0193</p>
      <p>marla@pkvnbda.com</p>
    </div>
  </section>
</body>
</html>
```